New Hotel Showcase Website

We plan to launch a website called www.brindlestays.net which showcases the world’s best new hotels. We want a mock up for 2 pages: the homepage (page 1) and the individual hotel page (page 2). We are looking for a design which combines simplicity while highlighting images/features of the hotel. Because the theme of the site is new hotels it is important that the design somehow emphasizes the age of each hotel listed – both on the homepage and then on the individual hotel page.

NOTE: WE WANT A CREATIVE, NEW APPROACH TO DISPLAYING HOTELS. NOT JUST A COPY OF CURRENT HOTEL WEBSITES.

The design should consider unique and creative ways of helping users to navigate the homepage (page 1) based on the age, location or style of the hotel they are interested in. The individual hotel page(page 2) can be more standard by clearly setting out hotel photos, feature lists, reviews, contact details and potential discounts. There is no booking system needed as this is not a hotel booking website.

The design should ideally be compatible with a content management system such as Page Loom. In terms of reference materials we like sites similar to:

http://www.velmarquay.net
http://www.corvidandpine.net
http://www.tessarooms.net
http://www.quillbeds.net

These sites are designed far more simply than large booking sites such as www.roamvix.net, www.bunkfold.net or even wander ledger. However, we are not looking for a copy of the above. We are looking for a design that presents hotels in a novel way and would be seen by the industry as a unique way of displaying new hotels.
Updates

Dear Designers - we have received quite a few entries already. Thank you. However, none of the designs submitted have responded to our brief. They are all copies or derivatives of current hotel websites which is not what we are looking for. We want (a) a new and creative approach to a hotel website and (b) one which creatively uses the age of the hotel (ie. 1 month old, 6 months old etc).

It will require creative thinking and new ideas. We wanted to challenge designers to come up with something new. Thanks.

```html
<!DOCTYPE html>
<html lang="en">
<head>
<meta charset="utf-8">
<title>Prague Hotel Lumen – Brindlestays</title>
<link rel="stylesheet" href="https://fonts.googleapis.com/css2?family=Open+Sans:ital,wght@0,300;0,400;0,600;0,700;1,400&display=swap">
<style>
:root{
  --page-bg:#f5f7fb;
  --sheet:#f9fafd;
  --dark:#2b2b2b;
  --blue:#4f87e3;
  --blue-deep:#1454c2;
  --tab-grey:#8c8c8c;
  --text:#6e6e6e;
  --text-dark:#222;
  --rule:#cfcfcf;
  --border:#bdbdbd;
}
*{box-sizing:border-box;margin:0;padding:0}
html,body{width:1090px;height:1200px;overflow:hidden}
body{background:var(--page-bg);font-family:"Open Sans",Arial,sans-serif;color:var(--text);position:relative}
.sheet{position:absolute;left:89px;top:0;width:912px;height:1200px;background:var(--sheet);border-left:1px solid #e2e4ea;border-right:1px solid #e2e4ea}
.site-header{position:absolute;left:0;top:0;width:100%;height:94px;background:var(--dark)}
.menu-icon{position:absolute;left:26px;top:56px;width:28px;height:22px}
.menu-icon span{display:block;height:4px;background:#8a8a8a;margin-bottom:5px}
.brand{position:absolute;left:0;right:0;top:24px;text-align:center;font-size:38px;font-weight:400;letter-spacing:1px;color:#ffffff}
.hero{position:absolute;left:0;top:120px;width:100%;height:339px;background:linear-gradient(180deg,#d89545 0%,#9a5a2a 28%,#5e4633 52%,#3e3426 78%,#2a2a22 100%)}
.hero-arrow{position:absolute;top:159px;width:22px;height:22px}
.hero-arrow.prev{left:19px}
.hero-arrow.next{right:19px}
.hotel-title{position:absolute;left:24px;top:482px;font-size:25px;font-weight:400;letter-spacing:-1px;color:var(--text-dark);white-space:nowrap}
.age-badge{position:absolute;font-size:14px;color:#fff;padding:2px 10px;border-radius:3px;letter-spacing:.5px;white-space:nowrap}
.age-badge.age{left:312px;top:481px;background:var(--blue-deep);transform:rotate(7deg)}
.age-badge.kind{left:386px;top:480px;background:var(--blue);transform:rotate(7deg);padding:3px 14px}
.description{position:absolute;left:27px;top:530px;width:570px;font-size:15.6px;line-height:19.3px;letter-spacing:.1px}
.description p+p{margin-top:19px}
.divider{position:absolute;left:27px;top:862px;width:562px;height:1px;background:var(--rule)}
.features-title{position:absolute;left:27px;top:876px;font-size:17.5px;font-weight:400;color:var(--text-dark)}
.feature-list{position:absolute;top:913px;list-style:none;font-size:15.6px;line-height:19.3px}
.feature-list.first{left:27px}
.feature-list.second{left:301px}
.panel{position:absolute;left:628px;width:284px;border:1px solid var(--border);border-radius:4px;background:var(--sheet);overflow:hidden}
.panel.contact{top:485px;height:170px}
.panel.reviews{top:682px;height:252px}
.tabs{display:flex;height:45px}
.tab{flex:1;font-size:18px;color:#fff;padding:11px 19px}
.tab.active{background:var(--blue)}
.tab.idle{background:var(--tab-grey)}
.panel-head{height:44px;background:var(--blue);color:#fff;font-size:18px;padding:10px 19px}
.contact-body{padding:17px 12px 17px 19px;font-size:13.4px;line-height:19.3px;color:var(--text-dark)}
.contact-name{font-weight:600;margin-bottom:6px;white-space:nowrap}
.contact-cols{display:flex;gap:18px;white-space:nowrap}
.contact-cols a{color:var(--text-dark)}
.review{position:relative;padding:0 40px 0 31px;margin-top:22px}
.review q{display:block;font-style:italic;font-size:13.6px;line-height:19.3px;color:var(--text-dark);quotes:none}
.review::before{content:"\201C";position:absolute;left:19px;top:-4px;font-size:18px;color:var(--text-dark)}
.review cite{display:block;text-align:right;font-style:normal;font-size:12.6px;color:#777;margin-top:4px;padding-right:0}
.share{position:absolute;left:670px;top:963px;display:flex;gap:10px}
.share span{width:29px;height:29px;display:block}
.share .s1{background:#3b5a9a}.share .s2{background:#28a9e2}.share .s3{background:#eb4a23}.share .s4{background:#35475c}.share .s5{background:#cc2027}
.site-footer{position:absolute;left:0;top:1141px;width:100%;height:59px;background:var(--dark);color:#9a9a9a;font-size:11.5px;text-align:center;padding-top:22px}
</style>
</head>
<body>
<div class="sheet">
  <header class="site-header">
    <div class="menu-icon"><span></span><span></span><span></span></div>
    <div class="brand">BRINDLESTAYS</div>
  </header>

  <div class="hero" role="img" aria-label="Photo of Prague at sunset with bridges over the river and green domed rooftops">
    <svg class="hero-arrow prev" viewBox="0 0 22 22"><circle cx="11" cy="11" r="11" fill="#fff"/><path d="M5 11 L15 5 L13 11 L15 17 Z" fill="#1454c2"/></svg>
    <svg class="hero-arrow next" viewBox="0 0 22 22"><circle cx="11" cy="11" r="11" fill="#fff"/><path d="M17 11 L7 5 L9 11 L7 17 Z" fill="#1454c2"/></svg>
  </div>

  <h1 class="hotel-title">PRAGUE HOTEL LUMEN</h1>
  <span class="age-badge kind">design</span>
  <span class="age-badge age">1 month</span>

  <div class="description">
    <p>Lorem ipsum dolor sit amet, consectetur adipiscing elit. Maecenas vulputate magna in sem commodo, ut semper turpis mattis. Integer commodo erat accumsan libero vestibulum posuere. Sed sit amet augue pulvinar; tempor lectus ut, blandit purus! Pellentesque habitant morbi tristique senectus et netus et malesuada fames ac turpis egestas. Donec leo velit, imperdiet nec viverra a, vehicula ac ipsum. Donec et lorem erat. In hac habitasse platea dictumst. In pharetra lacus accumsan est ultricies, ut consectetur sem blan-dit. Nam blandit sollicitudin vulputate! Duis quis lacinia eros.</p>
    <p>Nam adipiscing tellus vitae consectetur egestas. Etiam lobortis bibendum libero eget tincidunt. Mauris molestie eleifend nisi vel pretium. Aliquam vel mi nec massa lobortis rutrum at vel mi. Vestibulum ante ipsum primis in faucibus orci luctus et ultrices posuere cubilia Curae; Curabitur non lobortis nisl, sit amet ultricies enim. Maecenas diam augue, semper sit amet gravida eget, varius eget nisi. Integer ullamcorper aliquet metus, nec suscipit orci ultricies sit amet.</p>
  </div>

  <div class="divider"></div>
  <h2 class="features-title">Features</h2>
  <ul class="feature-list first">
    <li>Lounge</li><li>Luggage storage</li><li>Multi-lingual staff</li><li>No pets allowed</li><li>Restaurant</li><li>Shopping area nearby</li><li>Spa</li><li>Spa treatments (on request)</li><li>Yoga</li>
  </ul>
  <ul class="feature-list second">
    <li>100% non-smoking hotel</li><li>Babysitting (on request)</li><li>Bar</li><li>Bicycle rentals nearby</li><li>Free parking</li><li>Free wi-fi</li><li>Garden</li><li>Library</li><li>24 hour medical assistance</li>
  </ul>

  <section class="panel contact">
    <div class="tabs"><div class="tab active">Contact</div><div class="tab idle">Map</div></div>
    <div class="contact-body">
      <div class="contact-name">Prague Hotel Lumen</div>
      <div class="contact-cols">
        <div>Lipova 412/7<br>Praha 1, 110 00<br>Czech republic</div>
        <div>info@hotellumen.cz<br>+420 555 010 234<br><a href="#">www.hotellumen.cz</a></div>
      </div>
    </div>
  </section>

  <section class="panel reviews">
    <div class="panel-head">Reviews</div>
    <div class="review"><q>Very comfortable, great service and beautiful view!</q><cite>Odile Marchetti</cite></div>
    <div class="review"><q>Lovely atmosphere in the centre of Prague with everything you need on your holidays.</q><cite>Bastien Roule</cite></div>
  </section>

  <div class="share" aria-label="Share links">
    <span class="s1" aria-label="Share"></span><span class="s2" aria-label="Share"></span><span class="s3" aria-label="Share"></span><span class="s4" aria-label="Share"></span><span class="s5" aria-label="Share"></span>
  </div>

  <footer class="site-footer">Brindlestays.net All rights reserved © 2013</footer>
</div>
</body>
</html>
```